Personal coach needs brochure design for inspirational essay about authenticity

Overview:
I want a beautiful brochure, 11”x17” that folds to 8-1/2”x11” with 4 pages. Think of it as an oversize greeting card.
• Front cover: photograph of a dancer and title with attribution of quote (Pixavanto jpeg photo attached)
• Inside spread: Copy (Edith Sorrel copy attached) with some appropriate illustration, based on cover photo
• Back cover: contact information, brief descriptive copy, two small photos (jpeg photo attached; see copy for direction)
Copy for front cover title, inside spread and back cover is attached in doc titled "Edith Sorrel copy"

Purpose of brochure:
I'm a personal coach and once a year I produce a 4-page illustrated inspirational essay, which invites personal reflection on living a more mindful, meaningful life. Most people I send them to collect them. Someday in the future I'd like to put a collection of these essays into a coffee table book and also create a website for the collection, which is related to the personal coaching that I do.
I have the brochures printed hard copy. I have attached a few examples from previous years. Each has a unique design related to its theme.

Concept:
This year’s essay theme, “There will only ever be one you!” is based on a quote by Edith Sorrel, a famous modern dancer. The complete quote, which appears in the copy, is about being true to one’s authentic self. The essay is not about dance, but because the author of the quote was a dancer who personified this theme of being unique to self, I have selected a photo of dance for the cover.

Design Guidance:
Front cover: One possibility is to expand the background color of the Pixavanto photo so the photo seems to emerge from the background. But I am open to ideas. I think the photo is artsy enough as it is, but there may be other ways to treat it (e.g. special effects) that would also work. The title should appear somewhere. Make the attribution (--Edith Sorrel) in smaller type than the title.

Inside Spread: There may be ways to borrow a design motif from the cover photo to make the inside spread more visually interesting, i.e., not just straight copy. I think it may be helpful to make the font size of the quote larger than the rest of the copy, but it has to be read in sequence. Or maybe it's printed in same size as copy, but then also repeated and displayed by itself in larger type.

Back cover: If you look at some of the other examples I’ve sent, you’ll see how the back cover is typically handled. I want a reduced version of the cover to be placed near the line that says "this is the 16th in a series.." Then, there’s a jpeg photo of Edith Sorrel that should be placed next to the copy description of her.

Need extra days to review

```html
<!DOCTYPE html>
<html lang="en">
<head>
<meta charset="utf-8">
<title>There Will Only Ever Be One You – Essay Brochure</title>
<link rel="stylesheet" href="https://fonts.googleapis.com/css2?family=EB+Garamond:ital,wght@0,400;0,600;1,400;1,600&family=Cinzel:wght@400&family=Poppins:wght@400&display=swap">
<style>
  :root{
    --canvas:#e4e4e6;
    --page-dark:#1b1b1d;
    --page-mid:#2a2a2d;
    --ink-light:#e9e7e3;
    --ink-soft:#bdbab4;
    --gold:#d3a84e;
    --gold-soft:#c9b48a;
    --quote-grey:#8e8a84;
    --rule:#5a5752;
    --red:#d7141b;
  }
  *{margin:0;padding:0;box-sizing:border-box}
  html,body{width:863px;height:1200px;overflow:hidden;background:var(--canvas)}
  body{position:relative;font-family:"EB Garamond",Georgia,serif}

  .spread{position:absolute;left:20px;width:823px;height:532px;display:flex;box-shadow:0 6px 18px rgba(0,0,0,.25)}
  .spread--covers{top:45px}
  .spread--inside{top:622px}
  .page{position:relative;width:411.5px;height:532px;overflow:hidden;background:linear-gradient(160deg,var(--page-mid),var(--page-dark) 70%)}
  .page + .page{box-shadow:inset 10px 0 14px -8px rgba(0,0,0,.6)}

  /* back cover */
  .sheer-band{position:absolute;left:0;top:0;width:100%;height:200px}
  .thumb-cover{position:absolute;left:58px;top:150px;width:56px;height:76px;border:1px solid var(--gold);
    background:radial-gradient(circle at 55% 45%,#8c8d91,#3a3b3f 60%,#1d1d20)}
  .series-note{position:absolute;left:124px;top:150px;width:130px;font-size:7px;line-height:1.25;color:var(--ink-light)}
  .series-note em{color:var(--gold-soft);font-weight:600}
  .contact{position:absolute;left:58px;top:250px;font-size:6.4px;line-height:1.3;color:var(--ink-soft);font-style:italic}
  .contact__name{font-size:9px;color:var(--gold-soft);font-weight:600;font-style:italic}
  .contact__gap{margin-top:6px}
  .about-heading{position:absolute;left:58px;top:336px;font-size:8px;font-style:italic;font-weight:600;color:var(--gold-soft)}
  .portrait{position:absolute;left:58px;top:352px;width:122px;height:128px;border:1px solid var(--gold);
    background:radial-gradient(ellipse at 50% 60%,#a59e92 0,#4b4843 35%,#151516 75%)}
  .bio{position:absolute;left:196px;top:192px;width:190px;font-size:6.3px;line-height:1.32;color:var(--ink-light);font-style:italic;text-align:justify}
  .bio p + p{margin-top:7px}
  .bio strong{font-weight:600;font-style:normal}

  /* front cover */
  .cover-photo{position:absolute;inset:0;background:
      radial-gradient(ellipse at 62% 48%,#9c9ea3 0,#5e6066 30%,#2f3034 62%,#161618 100%)}
  .cover-frame{position:absolute;left:150px;top:108px;width:212px;height:330px;border:1.5px solid var(--gold)}
  .cover-title{position:absolute;left:96px;top:80px;font-family:"Cinzel",serif;font-size:15px;line-height:1.15;color:var(--ink-light);letter-spacing:.5px}
  .cover-title i{font-family:"EB Garamond",serif;font-size:16px}
  .cover-credit{position:absolute;left:316px;top:420px;transform:rotate(-90deg);transform-origin:left top;font-family:"Poppins",sans-serif;font-size:7.5px;letter-spacing:3px;color:var(--ink-light);white-space:nowrap}

  /* inside spread */
  .quote-rule{position:absolute;top:44px;left:34px;right:34px;height:20px}
  .essay{position:absolute;left:40px;top:86px;width:336px;font-size:8px;line-height:1.38;color:var(--ink-light);font-style:italic;text-align:justify}
  .essay p + p{margin-top:8px}
  .dancer-art{position:absolute;left:44px;top:88px;width:190px;height:230px;
    background:radial-gradient(ellipse at 55% 45%,var(--red) 0,rgba(215,20,27,.75) 22%,rgba(120,10,15,.35) 45%,rgba(0,0,0,0) 70%)}
  .pull-quote{position:absolute;left:232px;top:96px;width:150px;font-size:8.4px;line-height:1.3;color:var(--gold-soft);font-style:italic;text-align:right}
  .closing{position:absolute;left:40px;top:360px;width:342px;font-size:8px;line-height:1.38;color:var(--ink-light);font-style:italic;text-align:justify}
  .closing p + p{margin-top:8px}
</style>
</head>
<body>

<!-- Outer spread: back cover + front cover -->
<section class="spread spread--covers">
  <article class="page page--back">
    <svg class="sheer-band" viewBox="0 0 411 200" aria-hidden="true">
      <path d="M0 40 C120 80 200 10 411 60 L411 110 C220 70 140 150 0 110 Z" fill="#ffffff" opacity=".05"/>
      <path d="M0 70 C140 120 230 40 411 90" stroke="#ffffff" stroke-opacity=".08" fill="none"/>
    </svg>
    <div class="thumb-cover" role="img" aria-label="Reduced front cover: dancer leaping through dust inside a gold frame"></div>
    <p class="series-note"><em>There Will Only Ever Be One You</em> is the 16th in a series of Labor Day essays inviting a moment of reflection on living a more meaningful, more mindful life.</p>
    <div class="contact">
      <p><span class="contact__name">Lena Varga Holt,</span> Ph.D.</p>
      <p>Heron Point House</p>
      <p>18 Orchard Lane</p>
      <p>Eastbrook, Vermont 05601</p>
      <p class="contact__gap">Mobile: 802-555-0147</p>
      <p>Email: lena@vargaholt.net</p>
      <p class="contact__gap">©2023</p>
    </div>
    <p class="about-heading">“About Edith Sorrel”</p>
    <div class="portrait" role="img" aria-label="Black and white photograph of Edith Sorrel dancing in a flowing pale dress"></div>
    <div class="bio">
      <p>Born in 1894, Edith Sorrel danced and taught for over 70 years. She is recognized as a primal artistic force of the 20th century, whose influence on modernity has been compared to that of the great painters, writers, composers and architects of her age. Her themes dealt with the lives and conflicts of ordinary people, and she brought serious issues to the stage like war, poverty, intolerance and the injustices of slavery and mistreatment of native peoples. Rebelling against conventions of the past, her dancing and choreography exposed the depths of human emotion through intense movements that were forceful, stark, angular, jagged and percussive – startlingly unlike the formality of classical ballet, which she saw as antiquated.</p>
      <p><strong>About Photographer Clara Whitlow:</strong> In 1935 Clara Whitlow saw a performance by modern dancer and choreographer Edith Sorrel. Whitlow was so inspired by the dance performance that she introduced herself to Sorrel, and the two artists began an artistic collaboration that lasted more than 60 years. Whitlow often photographed dancers in action, to capture the emotion behind their movement. Her artistic style was in line with Sorrel’s philosophy of dance. This photo from the dance “Letter to the World,” is one of Whitlow’s most famous photographs. The title of this work comes from a Hollis Fenn poem, which inspired Sorrel to create a dance performance based on Fenn’s life.</p>
    </div>
  </article>

  <article class="page page--front">
    <div class="cover-photo" role="img" aria-label="Pixavanto photograph of a dancer in a dark satin dress leaping through a cloud of grey dust"></div>
    <div class="cover-frame"></div>
    <h1 class="cover-title">There will<br>only ever be<br>one <i>you!</i></h1>
    <p class="cover-credit">Edith Sorrel</p>
  </article>
</section>

<!-- Inner spread: essay -->
<section class="spread spread--inside">
  <article class="page page--essay-left">
    <svg class="quote-rule" viewBox="0 0 343 20" aria-hidden="true">
      <line x1="0" y1="10" x2="150" y2="10" stroke="var(--rule)" stroke-width=".6"/>
      <line x1="193" y1="10" x2="343" y2="10" stroke="var(--rule)" stroke-width=".6"/>
      <path d="M160 3 a5 5 0 1 1 4 9 q-1 5 -6 7 q3 -3 3 -6 a5 5 0 0 1 -1 -10z M175 3 a5 5 0 1 1 4 9 q-1 5 -6 7 q3 -3 3 -6 a5 5 0 0 1 -1 -10z" fill="var(--quote-grey)"/>
    </svg>
    <div class="essay">
      <p>In the rural village where I grew up, one of the highlights of Sunday morning church service – in between congregational hymn-singing and the preacher’s sermon – was the “special selection,” a musical performance by a parishioner. Typically, it was a vocalist or instrumental on piano, organ or violin. One Sunday, we were surprised by an unusual performance. A plump, buxom farm wife approached the pulpit, puckered up her lips and unexpectedly began to whistle the hymn “The Old Rugged Cross.” As a 10-year-old, I found this hilarious as I tried to choke back my wide-eyed amazement and giggles.</p>
      <p>Despite the irreverence of my pre-adolescent reaction, this memory has stayed with me for decades as an iconic example of the wonderment of individual differences. Of the delight I find in witnessing someone express herself in sometimes surprising and even courageous ways. Of the marvel of beholding a person be truly authentic and uniquely original.</p>
      <p>Someone who personified the irrepressible impulse to express her individuality was the early 20th century dancer and choreographer Edith Sorrel. A pioneer of modern dance, she threw tradition overboard and was inspired to dance in a way that was a radical departure from the formalized style and rigidly dictated forms of classical ballet. Sorrel felt compelled to express the rawness and emotion of human experience in her dancing – not just present a form of pretty entertainment. Iconoclastic and brilliant, she created a new language of dance, a revolutionary vocabulary of movement that electrified the stage, often creating a visceral response in the audience.</p>
      <p>In her biography of Sorrel, her friend and equally talented choreographer Ines Marlowe recalled that despite sensational reviews for her own innovative work in the Broadway musical <em>Prairie Song!</em>, Marlowe had a gnawing feeling that her work was only mediocre. Marlowe confessed her anxieties to Sorrel, who listened quietly and then responded: “There will only ever be one you!” Continuing, she added:</p>
    </div>
  </article>

  <article class="page page--essay-right">
    <svg class="quote-rule" viewBox="0 0 343 20" aria-hidden="true">
      <line x1="0" y1="10" x2="230" y2="10" stroke="var(--rule)" stroke-width=".6"/>
      <line x1="272" y1="10" x2="343" y2="10" stroke="var(--rule)" stroke-width=".6"/>
      <path d="M240 3 a5 5 0 1 1 4 9 q-1 5 -6 7 q3 -3 3 -6 a5 5 0 0 1 -1 -10z M255 3 a5 5 0 1 1 4 9 q-1 5 -6 7 q3 -3 3 -6 a5 5 0 0 1 -1 -10z" fill="var(--quote-grey)"/>
    </svg>
    <div class="dancer-art" role="img" aria-label="Red ink-splash illustration of a ballerina leaping, scattering red and pink droplets"></div>
    <blockquote class="pull-quote">“There is a vitality, a life-force, an energy, a quickening that is translated through you into action. And because there is only one of you in all of time, this expression is unique. And if you block it, it will never exist through any other medium and be lost. The world will not have it. It is not your business to determine how good it is nor how valuable nor how it compares with other expressions. It is your business to keep it yours clearly and directly, to keep the channel open. You have to keep open and aware directly to the urges that motivate you. Above all else, keep the channel open.”</blockquote>
    <div class="closing">
      <p>Sorrel’s wisdom reminds us that we must not hold back or judge our gifts. Although there may be moments when we doubt ourselves or when we worry that we’re not good enough, our job is to be fearless and to “keep the channel open.”</p>
      <p>Guard the precious miracle of your own uniqueness. Find that home-sweet-home feeling where you feel you are your most authentic self. There will only ever be one you! And importantly, respect the differences of others. Our world would be a drab, boring place if we all only whistled one tune.</p>
    </div>
  </article>
</section>

</body>
</html>
```